Business Card desgin, company called Stand Fast.

I am looking for the logo colors (3) to be used on the card in whatever design you think might work. the certifications are on the back (4) on the front will be my name, Dana Whitlock, owner/instructor, phone 208.555.0193, website www.sfx-drills.example, email dw@sfx-drills.example. im flexible on fonts.

Target Market(s)

firearms owners

Industry/Entity Type

firearms training

Contact Information for Business Card

certification icons on back

```html
<!DOCTYPE html>
<html lang="en">
<head>
<meta charset="utf-8">
<title>Stand Fast – Business Card</title>
<link rel="stylesheet" href="https://fonts.googleapis.com/css2?family=Montserrat:wght@400;500;600;700&family=Libre+Baskerville:wght@400&display=swap">
<style>
  :root {
    --stage: #3b3b3d;
    --navy: #0e2a47;
    --navy-raised: #1d4266;
    --navy-emboss: #2e5c82;
    --badge-neutral: #5a6f86;
    --red: #c11f2f;
    --white: #ffffff;
  }
  * { box-sizing: border-box; margin: 0; padding: 0; }
  html, body { width: 1200px; height: 689px; overflow: hidden; }
  body {
    background: var(--stage);
    font-family: "Montserrat", Arial, sans-serif;
    position: relative;
  }
  .card {
    position: absolute;
    top: 196px;
    width: 520px;
    height: 297px;
    border-radius: 16px;
    overflow: hidden;
    background: var(--navy);
  }
  .card--back { left: 50px; }
  .card--front { left: 630px; }

  /* Back side */
  .back-mark {
    position: absolute;
    left: 36px; top: 58px;
    width: 84px; height: 84px;
    border: 5px solid var(--navy-raised);
    border-radius: 50%;
  }
  .back-name {
    position: absolute;
    left: 142px; top: 60px;
    font-weight: 600;
    font-size: 40px;
    letter-spacing: 4px;
    color: var(--navy-emboss);
    white-space: nowrap;
  }
  .back-url {
    position: absolute;
    left: 146px; top: 112px;
    font-family: "Libre Baskerville", Georgia, serif;
    font-size: 18px;
    letter-spacing: 1px;
    color: var(--navy-raised);
    white-space: nowrap;
  }
  .badge {
    position: absolute;
    width: 56px; height: 56px;
    border-radius: 6px;
    background: var(--badge-neutral);
  }
  .badge--one { left: 40px; top: 216px; }
  .badge--two { left: 170px; top: 196px; }
  .badge--three { left: 300px; top: 176px; }
  .badge--four { left: 430px; top: 150px; }

  /* Front side */
  .front-top {
    position: absolute; left: 0; top: 0;
    width: 100%; height: 180px;
    background: var(--navy);
  }
  .front-rule {
    position: absolute; left: 0; top: 180px;
    width: 100%; height: 4px;
    background: var(--white);
  }
  .front-band {
    position: absolute; left: 0; top: 184px;
    width: 100%; height: 113px;
    background: var(--red);
  }
  .brand-name {
    position: absolute;
    left: 0; top: 30px; width: 100%;
    text-align: center;
    font-weight: 700;
    font-size: 20px;
    letter-spacing: 1px;
    color: var(--red);
  }
  .brand-circle {
    position: absolute;
    left: 216px; top: 64px;
    width: 88px; height: 88px;
    border: 8px solid var(--white);
    border-radius: 50%;
  }
  .holder {
    position: absolute;
    left: 30px; top: 212px;
    color: var(--white);
    text-align: right;
  }
  .holder-name { font-weight: 700; font-size: 26px; line-height: 1.1; }
  .holder-role { font-weight: 400; font-size: 14px; margin-top: 4px; }
  .divider {
    position: absolute;
    left: 246px; top: 206px;
    width: 1.5px; height: 64px;
    background: var(--white);
  }
  .contact {
    position: absolute;
    left: 264px; top: 208px;
    list-style: none;
    color: var(--white);
    font-size: 12.5px;
    font-weight: 500;
  }
  .contact li { display: flex; align-items: center; gap: 8px; height: 20px; }
  .contact svg { width: 11px; height: 11px; flex: none; }
</style>
</head>
<body>

<section class="card card--back" aria-label="Card back">
  <div class="back-mark"></div>
  <div class="back-name">STAND FAST</div>
  <div class="back-url">WWW.SFX-Drills.example</div>

  <div class="badge badge--one" role="img" aria-label="Certification badge"></div>
  <div class="badge badge--two" role="img" aria-label="Instructor certification badge"></div>
  <div class="badge badge--three" role="img" aria-label="Range safety certification badge"></div>
  <div class="badge badge--four" role="img" aria-label="Association certification badge"></div>
</section>

<section class="card card--front" aria-label="Card front">
  <div class="front-top"></div>
  <div class="front-rule"></div>
  <div class="front-band"></div>

  <div class="brand-name">STAND FAST</div>
  <div class="brand-circle"></div>

  <div class="holder">
    <div class="holder-name">Dana Whitlock</div>
    <div class="holder-role">owner/instructor</div>
  </div>
  <div class="divider"></div>

  <ul class="contact">
    <li>
      <svg viewBox="0 0 24 24" aria-hidden="true"><path fill="#fff" d="M6.6 10.8a15.1 15.1 0 0 0 6.6 6.6l2.2-2.2a1 1 0 0 1 1-.25 11.4 11.4 0 0 0 3.6.57 1 1 0 0 1 1 1V20a1 1 0 0 1-1 1A17 17 0 0 1 3 4a1 1 0 0 1 1-1h3.5a1 1 0 0 1 1 1c0 1.25.2 2.45.57 3.57a1 1 0 0 1-.25 1z"/></svg>
      208.555.0193
    </li>
    <li>
      <svg viewBox="0 0 24 24" aria-hidden="true"><rect x="2" y="5" width="20" height="14" fill="#fff"/><path d="M3 6l9 6 9-6" fill="none" stroke="#c11f2f" stroke-width="2"/></svg>
      dw@sfx-drills.example
    </li>
    <li>
      <svg viewBox="0 0 24 24" aria-hidden="true" fill="none" stroke="#fff" stroke-width="2.2"><circle cx="12" cy="12" r="9.5"/><path d="M2.5 12h19M12 2.5c3 3 3 16 0 19M12 2.5c-3 3-3 16 0 19"/></svg>
      www.sfx-drills.example
    </li>
  </ul>
</section>

</body>
</html>
```